Lumigrove Pages with Bold Font

I want the font to be simple yet bold for Lumigrove images. Its all about a simple bold readable font. I need a single lumigrove page with an image and copy/text on or over the image. The words will change in the future. I'm looking for the right font. I like fiery red and yellow colors. The "One Pic" attached is a sample of what I want without the Velnor words.

```html
<!DOCTYPE html>
<html lang="en">
<head>
<meta charset="utf-8">
<title>Mara Jean Cole — Fitness Trainer for Men</title>
<link href="https://fonts.googleapis.com/css2?family=Bebas+Neue&family=Poppins:wght@500;700;800&display=swap" rel="stylesheet">
<style>
  :root {
    --stage: #4d4d4d;
    --fire-red: #d3141b;
    --deep-red: #8e0a0e;
    --ember: #b01016;
    --gold: #eec41a;
    --white: #ffffff;
    --photo-warm: #7a3a26;
    --photo-deep: #5c1c14;
  }
  * { margin: 0; padding: 0; box-sizing: border-box; }
  html, body {
    width: 1200px;
    height: 902px;
    overflow: hidden;
    background: var(--stage);
  }
  .post {
    position: absolute;
    left: 169px;
    top: 20px;
    width: 862px;
    height: 862px;
    overflow: hidden;
    background:
      radial-gradient(ellipse at 70% 45%, var(--fire-red) 0%, var(--ember) 55%, var(--deep-red) 100%);
  }
  .post__texture {
    position: absolute;
    inset: 0;
    background: repeating-linear-gradient(
      178deg,
      rgba(0,0,0,0.06) 0px,
      rgba(0,0,0,0.06) 2px,
      rgba(255,255,255,0.03) 3px,
      rgba(255,255,255,0) 6px
    );
  }
  .post__photo {
    position: absolute;
    left: 0;
    top: 0;
    width: 400px;
    height: 862px;
    background: linear-gradient(180deg, var(--photo-warm) 0%, var(--photo-deep) 100%);
    -webkit-mask-image: linear-gradient(90deg, #000 0%, #000 70%, transparent 100%);
    mask-image: linear-gradient(90deg, #000 0%, #000 70%, transparent 100%);
  }
  .brand {
    position: absolute;
    right: 40px;
    top: 68px;
    text-align: left;
    color: var(--white);
    font-family: "Poppins", sans-serif;
  }
  .brand__name {
    font-weight: 800;
    font-size: 49px;
    line-height: 1;
    letter-spacing: 0.5px;
  }
  .brand__role {
    margin-top: 10px;
    font-weight: 500;
    font-size: 16.5px;
    letter-spacing: 7.4px;
    line-height: 1;
  }
  .headline {
    position: absolute;
    right: 38px;
    top: 0;
    font-family: "Bebas Neue", sans-serif;
    font-weight: 400;
    text-align: right;
    white-space: nowrap;
    line-height: 1;
  }
  .headline__line { display: block; }
  .headline__line--lead  { position: absolute; right: 0; top: 225px; font-size: 68px; color: var(--white); }
  .headline__line--hot   { position: absolute; right: 0; top: 285px; font-size: 100px; color: var(--white); }
  .headline__line--hard  { position: absolute; right: 0; top: 366px; font-size: 100px; color: var(--gold); }
  .headline__line--vegas { position: absolute; right: 0; top: 452px; font-size: 106px; color: var(--gold); }
  .headline__line--night { position: absolute; right: 0; top: 538px; font-size: 102px; color: var(--white); }
  .pitch {
    position: absolute;
    right: 40px;
    top: 680px;
    width: 660px;
    text-align: right;
    font-family: "Poppins", sans-serif;
    font-weight: 700;
    font-size: 21px;
    line-height: 28px;
    color: var(--white);
    white-space: nowrap;
  }
  .pitch__promise { margin-top: 28px; }
</style>
</head>
<body>
  <section class="post">
    <div class="post__photo" role="img" aria-label="Photo of a fitness model, cropped at the chin"></div>
    <div class="post__texture"></div>

    <header class="brand">
      <div class="brand__name">MARA JEAN COLE</div>
      <div class="brand__role">FITNESS TRAINER FOR MEN</div>
    </header>

    <h1 class="headline">
      <span class="headline__line headline__line--lead">HELPING MORE GUYS</span>
      <span class="headline__line headline__line--hot">GET HOT, SWEATY</span>
      <span class="headline__line headline__line--hard">&amp; HARD THAN A</span>
      <span class="headline__line headline__line--vegas">VEGAS HOOKER</span>
      <span class="headline__line headline__line--night">ON A FRIDAY NIGHT</span>
    </h1>

    <div class="pitch">
      <p class="pitch__question">YOU WANNA LOSE WEIGHT?&nbsp; YOU WANNA SHRINK THAT<br>GUT?&nbsp; TOUCH ME DOWN HERE.</p>
      <p class="pitch__promise">I CANHELP YOU SHRINK YOUR GUT.</p>
    </div>
  </section>
</body>
</html>
```